Redesign of Grantlyhub.com

We need a redesign of some key-pages on our crowdfunding website for mobile apps, GrantlyHub.com.

- Redesign of homepage
http://www.grantlyhub.com/en

- Redesign of project submission page
http://www.grantlyhub.com/en/submit-your-app/submit-your-app

- Redesign of browsing section
http://www.grantlyhub.com/en/fund-apps

- Redesign of project funding page
http://www.grantlyhub.com/en/fund-apps/sponsor/sketch-riddler?amount=5.00

Design should be highly focused on a great user experience for users of the platform, being in principal mobile developers. So we need a great user experience for mobile developers using our service.

Benchmark designs we particularly like are:
http://www.pledgorama.com/
http://www.tradebitly.com/landing/
http://www.vomba.com/

Design should have a more 'fun, happy to get involved' factor as it has nox.
Updates

Logo's have been uploaded

Target Market(s)

mobile app developers

Industry/Entity Type

Crowdfunding

Requirements
Must have
• Submission forms must have explanation fields next to the form

Homepage should have design in whihc a introductary video can be integrated

```html
<!DOCTYPE html>
<html lang="en">
<head>
<meta charset="utf-8">
<title>GrantlyHub – Crowdfunding Mobile Apps</title>
<link href="https://fonts.googleapis.com/css2?family=Carlito:wght@400;700&family=Mulish:wght@800&display=swap" rel="stylesheet">
<style>
:root{
  --page:#ebebeb;
  --ink:#222;
  --dark:#2b2b2b;
  --bezel:#1a1a1a;
  --brand:#1d5a96;
  --blue:#2f7fbf;
  --red:#c4161c;
  --green:#12a012;
  --hero-a:#4fb3d6;
  --hero-b:#74d3e4;
  --white:#fff;
  --partner:#8f8f8f;
}
*{box-sizing:border-box;margin:0;padding:0}
html,body{width:944px;height:1200px;overflow:hidden}
body{background:var(--page);font-family:"Carlito",Arial,sans-serif;color:var(--ink);position:relative}
.abs{position:absolute}

/* header */
.top-links{left:502px;top:11px;display:flex;align-items:center;font-size:12px;font-weight:700}
.top-links a{color:var(--ink);text-decoration:none;padding:0 5px;border-left:1px solid #999;line-height:12px}
.top-links a:first-child{border-left:none}
.search{margin-left:8px;width:88px;height:15px;background:#777;color:#ddd;font-weight:400;font-size:11px;text-align:center;border-radius:2px;line-height:15px}
.search-icon{margin-left:4px}
.brand{left:103px;top:30px;display:flex;align-items:center;gap:18px}
.brand-mark{width:90px;height:118px;background:var(--brand);border-radius:6px}
.brand-name{font-size:52px;color:var(--brand);font-weight:400;line-height:46px}
.social{top:53px;width:26px;height:26px;border-radius:50%;background:#111}

/* nav */
.nav{left:103px;top:193px;width:740px;height:46px;background:var(--dark);border-radius:6px 6px 0 0}
.nav ul{list-style:none;display:flex;gap:10px;position:absolute;left:7px;top:12px}
.nav li{background:#111;color:#fff;font-size:15px;padding:1px 7px;height:24px;line-height:22px;border-radius:3px}
.nav li.active{background:linear-gradient(#5aa7dc,#2f7fbf);font-weight:700}
.auth{top:183px;height:56px;width:59px;border-radius:8px 8px 0 0;color:#fff;font-weight:700;font-size:15px;text-align:center;padding-top:23px}
.login{left:687px;background:var(--red)}
.register{left:756px;width:69px;background:var(--green)}

/* hero */
.hero{left:0;top:239px;width:944px;height:234px;background:radial-gradient(ellipse at 75% 60%,var(--hero-b),var(--hero-a) 70%)}
.devices{left:103px;top:30px;width:360px;height:204px}
.device{position:absolute;bottom:0;background:var(--bezel);border-radius:16px 16px 0 0;padding:22px 8px 0}
.device .screen{width:100%;height:100%}
.hero h1{left:483px;top:46px;font-family:"Mulish",Arial,sans-serif;font-weight:800;font-size:26px;line-height:32px;color:#1d2a33;letter-spacing:-.5px}
.hero p{left:485px;top:123px;width:340px;font-size:13px;line-height:15px;color:#1d2a33}
.btn-red{background:var(--red);color:#fff;font-weight:700;border-radius:6px;text-align:center}
.learn{left:483px;top:182px;width:81px;height:22px;font-size:14px;line-height:22px}

/* tabs */
.tab{top:473px;height:36px;font-size:16px;font-weight:700;text-align:center;line-height:34px;border-bottom:3px solid var(--dark)}
.tab.active{background:var(--dark);color:#fff}

/* app cards */
.card{top:540px;width:107px;height:168px;background:#fff;box-shadow:0 1px 4px rgba(0,0,0,.35)}
.card .phone{height:100px;background:var(--bezel);border-radius:12px 12px 0 0;padding:18px 6px 0;border:1px solid #999;border-bottom:none}
.card .shot{height:100%}
.card .name{height:19px;background:var(--blue);color:#fff;font-size:10.5px;font-weight:700;text-align:center;line-height:19px}
.card p{font-size:9.5px;line-height:10.5px;text-align:center;padding:3px 8px}
.rule{left:104px;height:3px;width:485px;background:var(--blue)}
.see-all{left:528px;width:61px;height:20px;font-size:14px;line-height:20px;border-radius:3px}
h2{font-size:17px;font-weight:700;color:#333}

/* partners */
.partner{background:var(--partner)}

/* subscribe */
.field{left:294px;width:298px;height:27px;background:var(--dark);color:#fff;font-size:13px;font-weight:700;padding:6px 9px}

/* sidebar */
.side-head{left:607px;width:236px;display:flex;align-items:center;gap:6px;font-size:17px;font-weight:700;color:#333}
.side-head .line{flex:1;height:3px;background:var(--blue)}
.members{left:605px;display:grid;grid-template-columns:repeat(3,84px);row-gap:12px}
.member{text-align:center;font-size:11px;font-weight:700}
.avatar{width:50px;height:50px;margin:0 auto 2px;background:linear-gradient(#e6d6cc,#c9a08a 45%,#3b3550 80%)}

/* social box */
.likebox{left:614px;top:898px;width:218px;height:240px;background:#fff;border:1px solid #bbb;font-size:9px;padding:6px}
.likebox .lb-sq{position:absolute;left:8px;top:6px;width:32px;height:32px;background:var(--brand)}
.likebox .lb-title{font-size:12px;font-weight:700;color:var(--brand);margin-left:38px;line-height:13px}
.like-btn{margin:4px 0 0 38px;border:1px solid #999;width:36px;font-size:9px;text-align:center;background:#f2f2f2}
.fans{display:grid;grid-template-columns:repeat(4,40px);gap:4px 7px;margin-top:8px}
.fan div{width:40px;height:40px}
.fan span{display:block;font-size:8px;color:#555}
.lb-foot{position:absolute;bottom:4px;left:8px;font-size:8px;color:#555}

/* footer */
.footer{left:0;top:1169px;width:944px;height:31px;background:#000;color:#fff;font-size:15px;display:flex;justify-content:center;gap:28px;line-height:31px}
</style>
</head>
<body>

<nav class="top-links abs">
  <a href="#">Blog</a><a href="#">Get AAA Certified</a><a href="#">About us</a><a href="#">Search</a>
  <span class="search">Search site</span>
  <svg class="search-icon" width="20" height="18" viewBox="0 0 20 18"><circle cx="7" cy="7" r="5" fill="none" stroke="#333" stroke-width="2"/><line x1="11" y1="11" x2="18" y2="17" stroke="#333" stroke-width="3"/></svg>
</nav>

<div class="brand abs"><span class="brand-mark"></span><span class="brand-name">Grantly<br>Hub</span></div>
<span class="social abs" style="left:738px"></span>
<span class="social abs" style="left:778px"></span>
<span class="social abs" style="left:815px"></span>

<div class="nav abs">
  <ul>
    <li class="active">Home</li><li>Fund Apps</li><li>Submit your App</li><li>Find a Developer</li><li>How it Works</li>
  </ul>
</div>
<div class="auth login abs">Login</div>
<div class="auth register abs">Register</div>

<section class="hero abs">
  <div class="devices abs" role="img" aria-label="Three smartphones showing app home screens">
    <div class="device" style="left:0;width:110px;height:164px"><div class="screen" style="background:linear-gradient(#1b6fb8,#2a8fd6 50%,#0f3d66)"></div></div>
    <div class="device" style="left:92px;width:112px;height:186px"><div class="screen" style="background:linear-gradient(#3a3f55,#1a1d2a 60%,#5a2a2a)"></div></div>
    <div class="device" style="left:183px;width:148px;height:204px;background:#0e0e0e"><div class="screen" style="background:linear-gradient(#5e7fa8,#9cb6d2 40%,#6f5a7e)"></div></div>
  </div>
  <h1 class="abs">Store your company files in<br>our cloud now safer than ever.</h1>
  <p class="abs">Lorem Ipsum is simply dummy text of the printing and typesetting industry. Lorem Ipsum has been the industry's standard dummy text ever since the 1500s.</p>
  <div class="btn-red learn abs">Learn More</div>
</section>

<div class="tab active abs" style="left:103px;width:154px">Most funded Apps</div>
<div class="tab abs" style="left:260px;width:146px">Our staff's pick</div>
<div class="tab abs" style="left:408px;width:154px">Successfully Funded</div>

<article class="card abs" style="left:104px"><div class="phone"><div class="shot" role="img" aria-label="Sketched riddle game screen" style="background:linear-gradient(#2e2e2e,#1d1d1d)"></div></div><div class="name">Sketch Riddler</div><p>Lorem Ipsum is simply dummy text of the printing and type industry.</p></article>
<article class="card abs" style="left:229px"><div class="phone"><div class="shot" role="img" aria-label="Puzzle game screen" style="background:radial-gradient(circle at 50% 55%,#f0f0f0 0 18%,#c8161d 19%)"></div></div><div class="name">TileTwist</div><p>Lorem Ipsum is simply dummy text of the printing and type industry.</p></article>
<article class="card abs" style="left:355px"><div class="phone"><div class="shot" role="img" aria-label="Colourful city adventure game screen" style="background:linear-gradient(#8fd0ee,#bfe4f2 40%,#d99a5a 70%,#7bb0c4)"></div></div><div class="name">Lola's City Trip</div><p>Lorem Ipsum is simply dummy text of the printing and type industry.</p></article>
<article class="card abs" style="left:482px"><div class="phone"><div class="shot" role="img" aria-label="Orange app icon screen" style="background:radial-gradient(circle at 50% 55%,#f08a1c 0 30%,#303030 32%)"></div></div><div class="name">Zentrix</div><p>Lorem Ipsum is simply dummy text of the printing and type industry.</p></article>

<div class="rule abs" style="top:745px"></div>
<div class="btn-red see-all abs" style="top:736px">See All</div>

<h2 class="abs" style="left:107px;top:764px">Partners</h2>
<div class="partner abs" style="left:134px;top:810px;width:56px;height:56px;border-radius:50%;background:#a8a8a8"></div>
<div class="partner abs" style="left:248px;top:810px;width:70px;height:80px;border-radius:6px;background:#6a6a6a"></div>
<div class="partner abs" style="left:362px;top:820px;width:56px;height:56px;background:#7a7a7a"></div>
<div class="partner abs" style="left:482px;top:810px;width:56px;height:56px;border-radius:50%;background:#a8a8a8"></div>
<div class="partner abs" style="left:126px;top:926px;width:76px;height:76px;border-radius:50%;background:#7f7f7f"></div>
<div class="partner abs" style="left:256px;top:916px;width:66px;height:84px;border-radius:50%;background:#9a9a9a"></div>
<div class="partner abs" style="left:368px;top:928px;width:50px;height:66px;border-radius:6px;background:#777"></div>
<div class="partner abs" style="left:474px;top:926px;width:76px;height:76px;border-radius:50%;background:#7f7f7f"></div>

<div class="rule abs" style="top:1040px"></div>
<div class="btn-red see-all abs" style="top:1031px">See All</div>

<h2 class="abs" style="left:103px;top:1062px">Subscribe</h2>
<p class="abs" style="left:103px;top:1102px;width:180px;font-size:11px;line-height:12px">Lorem Ipsum is simply dummy text of the printing and type industry.</p>
<div class="field abs" style="top:1071px">Email</div>
<div class="field abs" style="top:1107px">Tel</div>

<aside>
  <div class="side-head abs" style="top:482px">Most active funders <span class="line"></span></div>
  <div class="members abs" style="top:522px">
    <div class="member"><div class="avatar" role="img" aria-label="Funder portrait"></div>Marcus D.</div>
    <div class="member"><div class="avatar" role="img" aria-label="Funder portrait"></div>Marcus D.</div>
    <div class="member"><div class="avatar" role="img" aria-label="Funder portrait"></div>Marcus D.</div>
    <div class="member"><div class="avatar" role="img" aria-label="Funder portrait"></div>Marcus D.</div>
    <div class="member"><div class="avatar" role="img" aria-label="Funder portrait"></div>Marcus D.</div>
    <div class="member"><div class="avatar" role="img" aria-label="Funder portrait"></div>Marcus D.</div>
  </div>

  <div class="side-head abs" style="top:680px">New Members <span class="line"></span></div>
  <div class="members abs" style="top:720px">
    <div class="member"><div class="avatar" role="img" aria-label="Member portrait"></div>Marcus D.</div>
    <div class="member"><div class="avatar" role="img" aria-label="Member portrait"></div>Marcus D.</div>
    <div class="member"><div class="avatar" role="img" aria-label="Member portrait"></div>Marcus D.</div>
    <div class="member"><div class="avatar" role="img" aria-label="Member portrait"></div>Marcus D.</div>
    <div class="member"><div class="avatar" role="img" aria-label="Member portrait"></div>Marcus D.</div>
    <div class="member"><div class="avatar" role="img" aria-label="Member portrait"></div>Marcus D.</div>
  </div>

  <div class="likebox abs">
    <span class="lb-sq"></span>
    <div class="lb-title">GrantlyHub - Crowdfunding Mobile Apps <span style="font-weight:400;font-size:9px">on Friendnet</span></div>
    <div class="like-btn">Like</div>
    <div style="margin-top:10px;border-top:1px solid #ddd;padding-top:4px">3,502 people like <b style="color:var(--brand)">GrantlyHub - Crowdfunding Mobile Apps.</b></div>
    <div class="fans">
      <div class="fan"><div role="img" aria-label="Fan picture" style="background:#c33"></div><span>Orvanta</span></div>
      <div class="fan"><div role="img" aria-label="Fan picture" style="background:#3a6fb0"></div><span>Brightloom</span></div>
      <div class="fan"><div role="img" aria-label="Fan picture" style="background:#5a3a4a"></div><span>Marisol</span></div>
      <div class="fan"><div role="img" aria-label="Fan picture" style="background:#a44"></div><span>Devika</span></div>
      <div class="fan"><div role="img" aria-label="Fan picture" style="background:#b99"></div><span>Anjali</span></div>
      <div class="fan"><div role="img" aria-label="Fan picture" style="background:#ccc"></div><span>Kelsey</span></div>
      <div class="fan"><div role="img" aria-label="Fan picture" style="background:#e5e5e5"></div><span></span></div>
      <div class="fan"><div role="img" aria-label="Fan picture" style="background:#6a7a3a"></div><span>Tarun</span></div>
    </div>
    <div class="lb-foot">Friendnet social plugin</div>
  </div>
</aside>

<footer class="footer abs">
  <span>Home</span><span>Fund Apps</span><span>Submit your App</span><span>Find a Developer</span><span>How it Works</span>
</footer>

</body>
</html>
```